Buch-Cover-Design - Lemurion 3.1 - Morgenlied für die Seele der Erdenkinder
Das Design von Glasfalke wurde sehr schnell und professionell erstellt. Ich habe mich außerordentlich gut betreut gefühlt, zumal die Designerin zum einen die Vorgabe excellent umgesetzt und dabei noch eigene Impulse eingebracht hat. Ich bin glücklich und dankbar, sowie hochzufrieden!
Zielgruppe
Ich habe ein Buch geschrieben. Zielgruppe sind Menschen mit dem Genre Spiritualität, Persönlichkeitsentwicklung, Esoterik, Coaching
Aufgabenstellung
Mein Buchtitel lautet: Lemurion 3.1 - Morgenlied für die Seele der Erdenkinder. Es sollte in irgendeiner Form ein spirituelles Cover sein. Gerne darf da auch die 'Lebensblume' als geometrisches Muster in einem Teil des Bildes integriert sein. Die Farben sollten eher hell, weiß, gelb und/oder rosa/lila sein. Keine dunklen Farben. Strahlen wie Sonnenlicht sind auch sehr gut.
Das Buch erscheint in DIN A5 und hat ca. 160 Seiten. Ich freue mich sehr über Ihre Vorschläge! Dankeschön.

```html
<!DOCTYPE html>
<html lang="de">
<head>
<meta charset="utf-8">
<title>Lemurion 3.1 – Buchcover</title>
<link href="https://fonts.googleapis.com/css2?family=Allura&family=Montserrat:wght@300;400&display=swap" rel="stylesheet">
<style>
  :root {
    --stage: #ece7e3;
    --paper: #ffffff;
    --spine-shade: #e9e9ec;
    --title: #ffffff;
    --subtitle: #e8528f;
    --author: #ffffff;
    --splash-orange: #f59a63;
    --splash-magenta: #e62fd0;
    --splash-violet: #c455ee;
    --splash-cyan: #6fdbe6;
    --brush-amber: #f4a41c;
    --brush-orange: #e8660f;
  }
  html, body {
    margin: 0;
    padding: 0;
    width: 1200px;
    height: 1188px;
    overflow: hidden;
    background: var(--stage);
  }
  .book-cover {
    position: absolute;
    left: 210px;
    top: 44px;
    width: 780px;
    height: 1100px;
    background: var(--paper);
    box-shadow: 0 18px 40px rgba(80, 60, 50, 0.18);
    overflow: hidden;
  }
  .book-cover::before {
    content: "";
    position: absolute;
    left: 0; top: 0; bottom: 0;
    width: 22px;
    background: linear-gradient(90deg, var(--spine-shade), var(--paper));
  }
  .watercolor-splash {
    position: absolute;
    left: 90px;
    top: 140px;
    width: 660px;
    height: 400px;
  }
  .book-title {
    position: absolute;
    left: 0; right: 0;
    top: 262px;
    margin: 0;
    text-align: center;
    font-family: "Allura", cursive;
    font-weight: 400;
    font-size: 104px;
    line-height: 1;
    color: var(--title);
    letter-spacing: 1px;
  }
  .book-subtitle {
    position: absolute;
    left: 0; right: 0;
    top: 522px;
    margin: 0;
    text-align: center;
    font-family: "Montserrat", sans-serif;
    font-weight: 300;
    font-size: 30px;
    line-height: 1.45;
    color: var(--subtitle);
  }
  .author-brush {
    position: absolute;
    left: 200px;
    top: 890px;
    width: 340px;
    height: 140px;
  }
  .author-name {
    position: absolute;
    left: 200px;
    top: 925px;
    width: 340px;
    margin: 0;
    text-align: center;
    font-family: "Allura", cursive;
    font-size: 52px;
    line-height: 1;
    color: var(--author);
  }
</style>
</head>
<body>
  <main class="book-cover">
    <svg class="watercolor-splash" viewBox="0 0 660 400" role="img" aria-label="Aquarellfleck in Orange, Magenta, Lila und Türkis mit Lebensblume-Muster">
      <defs>
        <linearGradient id="splash-tone" x1="0" y1="0.6" x2="1" y2="0.3">
          <stop offset="0" stop-color="var(--splash-orange)"/>
          <stop offset="0.3" stop-color="var(--splash-magenta)"/>
          <stop offset="0.7" stop-color="var(--splash-violet)"/>
          <stop offset="1" stop-color="var(--splash-cyan)"/>
        </linearGradient>
      </defs>
      <path fill="url(#splash-tone)" opacity="0.9"
        d="M40 150 C70 90 150 70 230 80 C300 40 380 30 450 50 C520 20 600 40 640 90 C660 130 630 160 600 175 C620 220 590 260 540 270 C520 320 470 350 420 330 C380 370 310 380 260 350 C200 370 130 350 100 310 C50 300 20 260 30 220 C10 200 15 170 40 150 Z"/>
    </svg>
    <h1 class="book-title">Lemurion 3.1</h1>
    <p class="book-subtitle">Morgenlied für die<br>Seele der Erdenkinder</p>
    <svg class="author-brush" viewBox="0 0 340 140" role="img" aria-label="Orangefarbener Pinselstrich">
      <defs>
        <linearGradient id="brush-tone" x1="0" y1="0" x2="1" y2="0">
          <stop offset="0" stop-color="var(--brush-amber)"/>
          <stop offset="1" stop-color="var(--brush-orange)"/>
        </linearGradient>
      </defs>
      <path fill="url(#brush-tone)"
        d="M20 60 C60 30 140 25 220 28 C270 24 320 35 330 60 C335 85 310 100 270 105 C210 115 130 118 70 112 C30 108 5 95 8 80 C10 70 14 66 20 60 Z"/>
    </svg>
    <p class="author-name">Name Autor</p>
  </main>
</body>
</html>
```